依頼詳細
《チラシのイメージ》
複数の写真やイラストの使用は避けてください。子育て世代向けへの広告とは一線画した差別化されたデザインを希望しています。また、子どもにフォーカスするのではなく、子育てママをフォーカスしていると一目でわかるビジュアルに仕上げてください。

※前回は塗り絵を前面に押しましたが、今回はその必要はありません。
(前回のチラシは添付データーをご参照ください)
理由は、前回は塗り絵に興味がある人への告知になってましたが、今回は子育てする親がセミナーに参加したくなるものにしてください。
《ターゲット》
お子さんの年齢は6歳以下の未就学児がいる中間層の子育て家族。

《デザインへの希望》
フォントのデザイン・文字サイズにメリハリをつけてください。
広告を見た瞬間に詳しく読みたくなるキャッチをメインにして「いつ開催?」「どこで開催?」は分かり易く見易く、その後、詳しく読みたくなる部分や、参加希望する人が必ず確認する部分については、小さな文字にしていただくことで、デザイン構成ください。

参加費無料や定員など、営業に映るような部分も、当会は堺貢献事業として活動している団体のため、営業的に映る部分については大きく目立つ表記は避けてください。さりげなく表記いただき、見れば分かる記述で結構です。

いろんな色を使用することで、ゴチャゴチャして大切な部分が見えなくなってしまうのは避けてください。

《セミナー構成》
前半:親への子育てセミナー
後半:子ども塗り絵診断

【キャッチ】
▮子どもと「ちょうどいい」距離感
または
▮子どもの世界をつくる
ママのひとり時間をつくる

【サブキャッチ】
▮子どもが言葉を話すようになったら...それは自分の世界を広げたいサイン

【リード文】
▮子育ての順番は「手を掛ける」「目を掛ける」「気を掛ける」どのタイミングでステップアップするかは、それぞれの子どもによって違う。子育てについて「周りは?」ついそう思ってしまいがち。周りを気にするのは誰かと比較してること。もっと色んな視点から子どもを見つめてみると見えてくるもの。早くから子どもの世界づくりをはじめ、親も自分時間を持つことで親子のちょうどいい距離感が生まれる。

【セミナー内容】
Lesson1ママパパ学び
・子どもの世界
・子どもの世界を広げるタイミング
・ヤル気のONスイッチ
・ちょうどいい子どもとの距離感
・子どもが成長してしまう3つのアプロ―チ
・子育て計画「コト・モノ・オカネ」

Lesson2子ども学び
・個性を見つける10の視点
・塗り絵診断
・子どもは天才の卵!
・生まれもった性格

【詳細】
テーマ:はじめての習いごと
開催日:8月24日(土)
時間:14時~16時
参加費:無料
定員:8家族(夫婦・親子でご参加ください)
開催場所:北嶺市民活動センター「ひだまる」
(兵庫県緑沢市緑野町桜台字松ノ木45-3)
対象者:子ども年齢/1歳2か月~6歳
(参加にはお申込みが必要です)
主催:そらいるか(一般社団法人家庭育成推進協会)
後援:緑沢市 緑沢市教育委員会
講師:そらいるか認定講師
受付:そらいるか事務局
〒541-0093大阪市中央区東浜町3-2-5-208
TEL0120-870-041
06-6912-4537    ※電話受付は平日9時~17時のみ
(メールは不要)

ホームページからのお申込みは▼
QRコード

記載項目
主催:そらいるか(一般社団法人家庭育成推進協会)
〒541-0093 大阪府大阪市中央区東浜町3-2-5-208
TEL:06-6912-4537 FAX:06-6912-4538
サイズ
A4
ページ数
片面
希望イメージ
シンプル 複雑
単色 カラフル
暗い 明るい
日常 高級
遊び心 厳粛
未来的 伝統的
女性的 男性的
希望する色
黄・オレンジ系
納品ファイル
• イラストレーター形式 (.ai)
補足説明
今回のセミナーは、過去に何度も開催しており、少しづつブラッシュアップしていってます。ワークポッドを利用するのは今回で2回目です。前回は21,600円でコンペに出しましたが、今回は要望内容が多いため54,000円でコンペに応募します。
現在、緑沢市と緑沢市教育委員会に後援申請をしています。後援の許可の有無により、後援名の部分の修正をお願いする可能性があります。またご提案いただいたチラシ内容は、法人の理事長の許可を必要としますので何度か修正をお願いすると思います。ご質問等がありましたら、ご連絡ください。

スッキリとまとまっており、一番目に飛び込んでくる構成になっているところが良かったです。
また、修正する場合に作業がしやすいデザインになっていると思えたところが良かったです。

沢山提案していただきありがとうございました。
また、こちらの都合で決めるのに時間がかかり申し訳ありませんでした。

```html
<!DOCTYPE html>
<html lang="ja">
<head>
<meta charset="utf-8">
<title>PAPA MAMA Seminar はじめての習いごと</title>
<link rel="stylesheet" href="https://fonts.googleapis.com/css2?family=M+PLUS+Rounded+1c:wght@400;700;800&family=Montserrat:wght@600;800&display=swap">
<style>
:root{
  --orange:#ef8a2b;
  --orange-deep:#e0701a;
  --peach:#fbdcbc;
  --peach-light:#fdeedd;
  --brown:#4b3b2f;
  --ink:#3a3330;
  --white:#ffffff;
  --line:#f3c79c;
}
*{margin:0;padding:0;box-sizing:border-box}
html,body{width:875px;height:1200px;overflow:hidden;background:var(--white)}
body{font-family:"M PLUS Rounded 1c",sans-serif;color:var(--ink)}
.flyer{position:relative;width:875px;height:1200px;overflow:hidden;background:var(--white)}
.hero{position:absolute;left:0;top:0;width:875px;height:530px;background:var(--peach)}
.tagline{position:absolute;top:18px;width:100%;text-align:center;color:var(--white);font-weight:800;font-size:22px;letter-spacing:4px}
.for-tag{position:absolute;left:165px;top:68px;width:50px;height:50px;border-radius:50%;border:3px solid var(--brown);font-family:"Montserrat",sans-serif;font-weight:800;font-size:17px;color:var(--brown);display:flex;align-items:center;justify-content:center;transform:rotate(-12deg)}
.title-en{position:absolute;left:0;width:100%;text-align:center;font-family:"Montserrat",sans-serif;font-weight:800;color:var(--brown);line-height:1;white-space:nowrap}
.title-en.main{top:68px;font-size:56px;letter-spacing:1px}
.title-en.sub{top:128px;font-size:42px}
.title-ja{position:absolute;top:188px;left:190px;width:495px;height:66px;display:flex;align-items:center;justify-content:center;font-weight:800;font-size:44px;color:var(--orange);letter-spacing:6px}
.title-ja::before,.title-ja::after{content:"";position:absolute;top:0;width:16px;height:66px;border:4px solid var(--orange)}
.title-ja::before{left:0;border-right:none}
.title-ja::after{right:0;border-left:none}
.art{position:absolute;border-radius:10px}
.art.book{left:715px;top:62px;width:95px;height:85px;background:linear-gradient(135deg,#fff6ec,#f5c79a)}
.art.piano{left:70px;top:262px;width:125px;height:95px;background:linear-gradient(135deg,#fff2e3,#e9b483)}
.art.racket{left:710px;top:240px;width:80px;height:125px;border-radius:40px;background:linear-gradient(135deg,#fff2e3,#f1b77f)}
.catch-card{position:absolute;left:210px;top:286px;width:455px;height:100px;background:var(--white);border-radius:14px;text-align:center;padding-top:16px;white-space:nowrap}
.catch-card .lead-in{font-size:18px;font-weight:700;color:var(--brown)}
.catch-card .sign{margin-top:10px;font-size:24px;font-weight:800;color:var(--brown)}
.catch-card .sign::before{content:"…";color:var(--orange);margin-right:4px}
.lead{position:absolute;left:110px;top:405px;width:655px;font-size:13.5px;line-height:1.75;color:var(--ink);text-align:center}
.theme{position:absolute;left:30px;top:548px;width:410px;height:36px;border:2px solid var(--orange);border-radius:18px;color:var(--orange);font-weight:800;font-size:19px;display:flex;align-items:center;justify-content:center}
.date{position:absolute;left:38px;top:592px;color:var(--orange);font-weight:800;font-size:78px;line-height:1;letter-spacing:-2px}
.date small{font-size:46px}
.date .dow{font-size:34px;letter-spacing:0}
.time{position:absolute;left:40px;top:686px;font-weight:700;font-size:22px;color:var(--brown)}
.time span{font-size:14px}
.fee{position:absolute;left:40px;top:728px;width:120px;height:38px;border-radius:19px;background:var(--orange);color:var(--white);font-weight:800;font-size:17px;display:flex;align-items:center;justify-content:center}
.capacity{position:absolute;left:190px;top:720px;font-weight:800;color:var(--brown);font-size:22px}
.capacity b{color:var(--orange);font-size:34px}
.capacity small{display:block;font-size:11px;font-weight:400}
.details{position:absolute;left:462px;top:548px;width:385px;border-collapse:collapse;font-size:12.5px}
.details th{width:82px;background:var(--orange);color:var(--white);font-weight:700;padding:5px 4px;border-bottom:2px solid var(--white);vertical-align:middle}
.details td{padding:5px 10px;border-bottom:1px solid var(--line);line-height:1.45}
.details td small{font-size:10.5px}
.section-bar{position:absolute;left:30px;top:800px;width:815px;height:30px;background:var(--peach);border-radius:15px;text-align:center;font-weight:800;color:var(--brown);font-size:16px;line-height:30px}
.lesson{position:absolute;top:840px;width:395px;height:210px;border:2px solid var(--line);border-radius:14px;padding:12px 14px}
.lesson.parent{left:30px}
.lesson.child{left:450px}
.lesson h3{display:flex;align-items:center;gap:8px;font-size:20px;font-weight:800;color:var(--brown)}
.lesson h3 .no{background:var(--orange);color:var(--white);font-family:"Montserrat",sans-serif;font-size:12px;border-radius:12px;padding:3px 10px}
.lesson ul{list-style:none;margin-top:8px;font-size:13px;line-height:1.62;width:240px;white-space:nowrap}
.lesson li::before{content:"●";color:var(--orange);font-size:8px;margin-right:5px;vertical-align:2px}
.lesson .art{right:12px;bottom:14px;width:112px;height:125px}
.art.parents{background:linear-gradient(135deg,#fff3e6,#f0b47c)}
.art.kids{background:linear-gradient(135deg,#fff3e6,#eea868)}
.footer{position:absolute;left:0;top:1062px;width:875px;height:138px;background:var(--peach-light);border-top:3px solid var(--orange)}
.brand{position:absolute;left:30px;top:18px;display:flex;align-items:center;gap:10px}
.brand .mark{width:58px;height:58px;border-radius:50%;background:var(--orange)}
.brand .name{font-weight:800;font-size:20px;color:var(--brown)}
.org{position:absolute;left:30px;top:84px;font-size:10.5px;line-height:1.5;color:var(--ink)}
.reception{position:absolute;left:290px;top:16px;width:390px;display:flex;align-items:flex-start;gap:10px}
.reception .label{display:block;flex:0 0 26px;width:26px;background:var(--orange);color:var(--white);font-weight:800;font-size:13px;writing-mode:vertical-rl;text-align:center;line-height:26px;padding:6px 0;border-radius:6px}
.reception .office{font-weight:800;font-size:18px;color:var(--brown)}
.reception .note{font-size:10.5px;color:var(--ink);line-height:1.4}
.phone{position:absolute;left:330px;top:80px;display:flex;align-items:center;gap:8px;font-family:"Montserrat",sans-serif;font-weight:800;font-size:32px;color:var(--orange-deep);white-space:nowrap}
.phone .sub{font-size:14px;color:var(--brown);margin-left:8px}
.apply{position:absolute;right:24px;top:26px;width:150px;font-size:11.5px;text-align:center;color:var(--brown);font-weight:700;line-height:1.6}
</style>
</head>
<body>
<main class="flyer">
  <section class="hero">
    <p class="tagline">子どもの世界をつくる ママのひとり時間をつくる</p>
    <div class="for-tag">for</div>
    <h1 class="title-en main">PAPA MAMA</h1>
    <p class="title-en sub">Seminar</p>
    <h2 class="title-ja">はじめての習いごと</h2>
    <div class="art book" role="img" aria-label="本のイラスト"></div>
    <div class="art piano" role="img" aria-label="ピアノと音符のイラスト"></div>
    <div class="art racket" role="img" aria-label="テニスラケットのイラスト"></div>
    <div class="catch-card">
      <p class="lead-in">子どもが言葉を話すようになったら…</p>
      <p class="sign">それは自分の世界を広げたいサイン</p>
    </div>
    <p class="lead">子育ての順番は「手を掛ける」「目を掛ける」「気を掛ける」どのタイミングでステップアップするかは、それぞれの子どもによって違う。子育てについて「周りは？」ついそう思ってしまいがち。周りを気にするのは誰かと比較してること。もっと色んな視点から子どもを見つめてみると見えてくるもの。早くから子どもの世界づくりをはじめ、親も自分時間を持つことで親子のちょうどいい距離感が生まれる。</p>
  </section>

  <p class="theme">テーマ：はじめての習いごと</p>
  <p class="date">8<small>月</small>24<small>日</small><span class="dow">(土)</span></p>
  <p class="time">時間：14:00-16:00 <span>(2時間)</span></p>
  <p class="fee">参加費無料</p>
  <p class="capacity">定員：<b>8</b>家族<small>(夫婦・親子でご参加ください)</small></p>

  <table class="details">
    <tr><th>開催場所</th><td>北嶺市民活動センター「ひだまる」<br><small>(兵庫県緑沢市緑野町桜台字松ノ木45-3)</small></td></tr>
    <tr><th>対象者</th><td>子ども年齢/1歳2か月〜6歳<br><small>(参加にはお申込みが必要です)</small></td></tr>
    <tr><th>主催</th><td>そらいるか<br><small>(一般社団法人家庭育成推進協会)</small></td></tr>
    <tr><th>後援</th><td>緑沢市 緑沢市教育委員会</td></tr>
    <tr><th>講師</th><td>そらいるか認定講師</td></tr>
  </table>

  <p class="section-bar">セミナー内容</p>
  <section class="lesson parent">
    <h3><span class="no">Lesson 1</span>ママパパ学び</h3>
    <ul>
      <li>子どもの世界</li>
      <li>子どもの世界を広げるタイミング</li>
      <li>ヤル気のONスイッチ</li>
      <li>ちょうどいい子どもとの距離感</li>
      <li>子どもが成長する3つのアプローチ</li>
      <li>子育て計画「コト・モノ・オカネ」</li>
    </ul>
    <div class="art parents" role="img" aria-label="親子のイラスト"></div>
  </section>
  <section class="lesson child">
    <h3><span class="no">Lesson 2</span>子ども学び</h3>
    <ul>
      <li>個性を見つける10の視点</li>
      <li>塗り絵診断</li>
      <li>子どもは天才の卵！</li>
      <li>生まれもった性格</li>
    </ul>
    <div class="art kids" role="img" aria-label="塗り絵をする子どものイラスト"></div>
  </section>

  <footer class="footer">
    <div class="brand"><span class="mark"></span><span class="name">そらいるか</span></div>
    <p class="org">一般社団法人家庭育成推進協会<br>〒541-0093大阪市中央区東浜町3-2-5-208</p>
    <div class="reception">
      <span class="label">受付</span>
      <div>
        <p class="office">そらいるか事務局</p>
        <p class="note">お電話・ホームページからお申込みください<br>※電話受付は平日9時〜17時のみ</p>
      </div>
    </div>
    <p class="phone">
      <svg width="28" height="28" viewBox="0 0 24 24" aria-hidden="true"><path fill="currentColor" d="M6.6 10.8a15.1 15.1 0 0 0 6.6 6.6l2.2-2.2c.3-.3.7-.4 1-.2 1.1.4 2.3.6 3.6.6.6 0 1 .4 1 1V20c0 .6-.4 1-1 1A17 17 0 0 1 3 4c0-.6.4-1 1-1h3.5c.6 0 1 .4 1 1 0 1.3.2 2.5.6 3.6.1.3 0 .7-.2 1z"/></svg>
      0120-354-926<span class="sub">(06-6912-4537)</span>
    </p>
    <p class="apply">ホームページからの<br>お申込みはこちら▼</p>
  </footer>
</main>
</body>
</html>
```